Pediatric Vision Care: Myopia Control Brochure

We are a pediatric eye care practice (ophthalmology and optometry). One of our services we offer for children is myopia control, which are strategies for slowing or stopping the progression of nearsightedness. This is a service we need to sell to parents because most insurance won't pay for it. There are different options we offer that can work well for kids in different situations: glasses with Corvane lenses, atropine eye drops, and/or special contact lenses. We need a brochure we can distribute to parents to let them know about this service that would encourage them to buy it for children who need it. Attached is our initial draft brochure created by our staff that provides text that we want to keep. The images and layout can change. We probably need at least one or two photos of kids on the brochure, because this is only something that works for children who are still growing, and the target audience is parents of 4-8 year old children.

Target Market(s)

Parents of 4-8 year old children

Font styles to use
Sans Serif

Requirements
Must have
• I'm uploading our company logo that should be included somewhere on the brochure. You can include contact information (web address, phone number) for our practice that is found on our website: http://www.brookhollowkidsvision.com/
Should not have
• This should not look childish. We need the impression to be friendly but professional, medical, expert.

```html
<!DOCTYPE html>
<html lang="en">
<head>
<meta charset="utf-8">
<title>Myopia Control Brochure</title>
<link href="https://fonts.googleapis.com/css2?family=Montserrat:wght@400;500;600;700&display=swap" rel="stylesheet">
<style>
  :root {
    --bg: #bcbde0;
    --panel-green: #eef3d8;
    --panel-peach: #fae5d0;
    --brand-green: #8cc412;
    --brand-orange: #f07d12;
    --brand-blue: #6677d6;
    --brand-yellow: #f9c21a;
    --ink: #222226;
    --body: #3b3b40;
    --white: #ffffff;
  }
  * { box-sizing: border-box; margin: 0; padding: 0; }
  html, body { width: 1200px; height: 800px; overflow: hidden; }
  body {
    background: var(--bg);
    font-family: "Montserrat", Arial, sans-serif;
    color: var(--body);
    position: relative;
  }
  .inside-spread {
    position: absolute; left: 40px; top: 110px;
    width: 810px; height: 580px;
    display: flex;
    box-shadow: 0 8px 24px rgba(60,60,100,.25);
  }
  .panel { position: relative; width: 270px; height: 580px; padding: 0 20px; font-size: 9.2px; line-height: 1.55; }
  .panel--green { background: var(--panel-green); }
  .panel--divider { border-left: 1px solid rgba(0,0,0,.06); }
  .panel--peach { background: var(--panel-peach); padding: 0; }
  .rule { position: absolute; top: 38px; height: 4px; }
  .rule--green { left: 20px; width: 520px; background: var(--brand-green); }
  .rule--orange { left: 0; width: 250px; background: var(--brand-orange); }
  .section-title { font-size: 15px; font-weight: 700; color: var(--ink); }
  .panel-one .section-title { padding-top: 66px; margin-bottom: 16px; }
  .pill {
    display: inline-block; background: var(--brand-green); color: var(--white);
    font-weight: 600; font-size: 10.5px; padding: 3px 10px; border-radius: 0 10px 10px 0;
    margin-bottom: 10px;
  }
  .image-block { border-radius: 3px; }
  .image-block--right { float: right; margin-left: 10px; }
  .image-block--left { float: left; margin-right: 10px; }
  .lens-photo { width: 112px; height: 104px; background: linear-gradient(135deg, #a8dbe8, #3a9cc0); }
  .drops-photo { width: 116px; height: 122px; background: linear-gradient(160deg, #e8f2fb, #7da8d6); }
  .contact-photo { width: 108px; height: 112px; background: linear-gradient(135deg, #d4e8f4, #e8b89c); }
  .exam-photo { width: 236px; height: 254px; margin-top: 88px; margin-bottom: 26px; background: linear-gradient(120deg, #d9d2cb, #8d8a86 60%, #f0eeeb); }
  .outdoor-photo { position: absolute; left: 0; bottom: 0; width: 270px; height: 170px; background: linear-gradient(180deg, #c7dbe6, #5f8a3e 45%, #7ab04a); }
  .clear { clear: both; }
  .block { margin-bottom: 10px; }
  .after-image { margin-top: 8px; }
  .section-gap { margin-top: 24px; }
  .env-content { padding: 64px 20px 0; }
  .env-content .section-title { margin-bottom: 8px; }
  .env-content p { margin-bottom: 12px; }
  .highlight { color: var(--brand-orange); font-weight: 600; }

  .cover {
    position: absolute; left: 890px; top: 110px;
    width: 270px; height: 580px; background: var(--white);
    box-shadow: 0 8px 24px rgba(60,60,100,.25);
  }
  .brand-mark { position: absolute; top: 36px; right: 18px; display: flex; align-items: center; gap: 6px; }
  .brand-dot { width: 12px; height: 12px; border-radius: 50%; background: var(--brand-green); }
  .brand-name { font-size: 12px; font-weight: 600; color: var(--ink); }
  .cover-photo { position: absolute; left: 46px; top: 80px; width: 210px; height: 350px; background: linear-gradient(180deg, #8f94dc, #a2a6e2); }
  .cover-title { position: absolute; left: 34px; top: 452px; font-size: 28px; font-weight: 600; color: var(--ink); letter-spacing: .2px; }
  .cover-tagline { position: absolute; left: 34px; top: 530px; font-size: 8.5px; font-weight: 500; color: var(--ink); }
  .color-bar { position: absolute; left: 34px; right: 0; bottom: 10px; height: 12px; display: flex; }
  .color-bar span { flex: 1; }
  .bar-blue { background: var(--brand-blue); }
  .bar-green { background: var(--brand-green); }
  .bar-yellow { background: var(--brand-yellow); }
  .bar-orange { background: var(--brand-orange); }
</style>
</head>
<body>
  <main class="inside-spread">
    <section class="panel panel--green panel-one">
      <div class="rule rule--green"></div>
      <h2 class="section-title">Several treatment options</h2>
      <div class="pill">Lumeris Corvane glasses lenses</div>
      <div class="block">
        <div class="image-block image-block--right lens-photo" role="img" aria-label="Close-up of a myopia control spectacle lens"></div>
        <p>FDA market authorized Lumeris Corvane glasses lenses have been shown to slow myopia progression by about 50% in children aged 6-12.</p>
        <div class="clear"></div>
        <p class="after-image">These lenses are a great treatment option because all your child needs to do is wear glasses. They look almost identical to ordinary glasses, but use specialized optics to signal the brain to slow the growth of myopic eyes.</p>
      </div>
      <div class="section-gap">
        <div class="pill">Low-dose atropine</div>
        <div class="image-block image-block--left drops-photo" role="img" aria-label="Eye drop falling from a dropper bottle"></div>
        <p>These eyedrops have been studied for over 20 years and have been shown to slow myopia progression by about 50% when used consistently.</p>
        <div class="clear"></div>
        <p class="after-image">Atropine is simple to add to your daily routine. One drop is placed in each eye before bed each evening. These are ordered from a compounding pharmacy and mailed directly to your home.</p>
      </div>
    </section>

    <section class="panel panel--green panel--divider">
      <div class="exam-photo image-block" role="img" aria-label="Young girl having an eye exam at a slit lamp with an eye doctor"></div>
      <div class="pill">Specialty contact lenses</div>
      <div class="image-block image-block--right contact-photo" role="img" aria-label="Soft contact lens on a fingertip"></div>
      <p>FDA-approved ClearPath lenses have been shown to slow myopia progression by about 50% in children aged 8-12. Contact lenses can be a great fit for many children, especially active children or those who do not enjoy wearing glasses. Many children as young as 7 or 8 are successful at wearing contacts.</p>
    </section>

    <section class="panel panel--peach">
      <div class="rule rule--orange"></div>
      <div class="env-content">
        <h2 class="section-title">Environmental options</h2>
        <p>All myopic children can benefit from these lifestyle changes.</p>
        <p>It is important to get your child <span class="highlight">outdoors</span> consistently. There is strong evidence that children who spend at least <span class="highlight">2 hours a day</span> outdoors are less likely to become myopic, and their myopia progresses slower than children who are outdoors less. Some studies show that increasing outdoor time by as few as 45 minutes a day is beneficial in reducing progression.</p>
        <p>There is some evidence that consistent use of screens, particularly held very close to the face, can worsen nearsightedness. We recommend limiting non-academic screen time and near work, and encourage your child to use the <span class="highlight">20-20-20 rule</span>. Every 20 minutes take a 20 second break to look at least 20 feet away.</p>
      </div>
      <div class="outdoor-photo" role="img" aria-label="Children running across a sunny grassy park"></div>
    </section>
  </main>

  <section class="cover">
    <div class="brand-mark">
      <span class="brand-dot"></span>
      <span class="brand-name">Brookhollow Kids Vision</span>
    </div>
    <div class="cover-photo" role="img" aria-label="Smiling girl wearing clear-framed glasses"></div>
    <h1 class="cover-title">Myopia Control</h1>
    <p class="cover-tagline">Every child deserves to see the world clearly</p>
    <div class="color-bar">
      <span class="bar-blue"></span><span class="bar-green"></span><span class="bar-yellow"></span><span class="bar-orange"></span>
    </div>
  </section>
</body>
</html>
```